I need a graphic for the promotion email for our "5th Yearly Crisis Preparedness Skills Camp" that incorporates our current logo and brand theme. I would like this graphic to funnel potentional attendees to register for a course. My perference would include a cool fire photo from our facility for the background. More information can be found on Marlowfieldcrew.com and also our Facebook.

```html
<!DOCTYPE html>
<html lang="en">
<head>
<meta charset="utf-8">
<title>5th Yearly Crisis Preparedness Skills Camp</title>
<link rel="stylesheet" href="https://fonts.googleapis.com/css2?family=Oswald:wght@500;600&family=Open+Sans:wght@400;600;700&display=swap">
<style>
:root{
  --orange:#e8401c;
  --ink:#111111;
  --white:#ffffff;
  --slate:#22282c;
  --rule:#4a5258;
  --card-shadow:rgba(0,0,0,.14);
  --icon-tone:#cfd8dc;
}
*{margin:0;padding:0;box-sizing:border-box}
html,body{width:1200px;height:2310px;overflow:hidden;background:var(--white)}
body{font-family:"Open Sans",sans-serif;color:var(--ink);position:relative}

.hero{position:absolute;left:0;top:0;width:1200px;height:800px;overflow:hidden}
.hero-photo{position:absolute;inset:0;
  background:
    radial-gradient(ellipse 260px 300px at 720px 260px,rgba(232,110,40,.75),rgba(232,110,40,0) 70%),
    radial-gradient(ellipse 340px 520px at 880px 520px,rgba(20,22,24,.95),rgba(20,22,24,0) 75%),
    linear-gradient(100deg,#3b3f46 0%,#55585e 40%,#7b8797 70%,#b9c3cf 100%);}
.brand-mark{position:absolute;left:200px;top:150px;width:320px;display:flex;flex-direction:column;align-items:center;gap:14px}
.brand-dot{width:84px;height:84px;border-radius:50%;border:5px solid var(--orange)}
.brand-name{font-family:"Open Sans",sans-serif;font-weight:700;font-size:30px;letter-spacing:4px;color:var(--white)}
.hero-text{position:absolute;left:40px;width:640px;top:360px;text-align:center;color:var(--white)}
.edition{display:flex;align-items:center;justify-content:center;gap:18px;font-family:"Oswald",sans-serif;font-weight:500;font-size:40px;line-height:50px}
.edition::before,.edition::after{content:"";width:150px;height:1px;background:rgba(255,255,255,.6)}
.edition sup{font-size:22px}
.title-top{font-family:"Oswald",sans-serif;font-weight:600;font-size:64px;line-height:78px;color:var(--orange);margin-top:4px}
.title-bottom{font-family:"Oswald",sans-serif;font-weight:600;font-size:66px;line-height:74px}
.tagline{font-size:27px;line-height:34px;color:var(--orange);margin-top:6px}
.when{font-size:27px;line-height:40px;margin-top:4px}
.motto{font-size:20px;margin-top:64px}

.features{position:absolute;left:0;top:800px;width:1200px;height:624px;background:var(--white)}
.features h2{position:absolute;top:52px;width:100%;text-align:center;font-weight:700;font-size:50px;line-height:62px}
.cards{position:absolute;top:228px;left:151px;display:flex;gap:37px}
.card{width:275px;height:344px;background:var(--white);box-shadow:0 2px 8px var(--card-shadow);padding:36px 14px 0;text-align:center}
.card-icon{width:120px;height:110px;margin:0 auto 14px;border-radius:50%;background:var(--icon-tone)}
.card h3{font-weight:600;font-size:26px;line-height:31px}
.card p{font-size:17.5px;line-height:21px;margin-top:8px;text-align:left;padding:0 2px}

.cta{position:absolute;left:0;top:1424px;width:1200px;height:684px;background:var(--slate);color:var(--white);text-align:center}
.cta h2{margin-top:100px;font-weight:700;font-size:50px;line-height:60px}
.cta .secure{font-size:50px;line-height:62px}
.cta .contact-link{display:inline-block;margin-top:4px;font-size:31px;color:var(--white);text-decoration:underline;text-underline-offset:4px}
.cta hr{width:830px;margin:36px auto 0;border:0;border-top:1px solid var(--rule)}
.cta .urgency{margin-top:44px;font-size:36px;line-height:42px}
.register{display:inline-block;margin-top:40px;width:258px;height:65px;line-height:65px;background:var(--orange);color:var(--white);font-weight:600;font-size:30px;text-decoration:none;box-shadow:0 0 10px rgba(232,64,28,.6)}
.cta .or{margin-top:18px;font-size:18px;font-weight:600}
.cta .details{font-size:18px;font-weight:600;margin-top:4px}

.footer{position:absolute;left:0;top:2108px;width:1200px;height:202px;background:var(--white)}
.footer-brand{position:absolute;left:100px;top:74px;display:flex;align-items:center;gap:10px}
.footer-brand .brand-dot{width:58px;height:58px;border-width:3px}
.footer-brand .brand-name{color:var(--ink);font-size:22px;letter-spacing:3px}
.contact{position:absolute;left:470px;top:76px;font-size:28px;line-height:35px}
.contact div{display:flex;align-items:center;gap:18px}
.contact svg{width:32px;height:28px}
.social{position:absolute;left:918px;top:82px;display:flex;gap:30px}
.social span{width:41px;height:41px;border-radius:50%;background:var(--ink)}
</style>
</head>
<body>

<header class="hero">
  <div class="hero-photo" role="img" aria-label="Photo of an instructor in turnout gear watching a live fire training blaze at the facility"></div>
  <div class="brand-mark">
    <span class="brand-dot"></span>
    <span class="brand-name">MARLOWFIELD CREW</span>
  </div>
  <div class="hero-text">
    <div class="edition"><span>5<sup>TH</sup> YEARLY</span></div>
    <div class="title-top">CRISIS PREPAREDNESS</div>
    <div class="title-bottom">SKILLS CAMP</div>
    <div class="tagline">REAL-WORLD FIRE &amp; INDUSTRIAL<br>EMERGENCY TRAINING</div>
    <div class="when">FALL 2026 | HOUSTON FACILITY</div>
    <div class="motto">ADVANCE YOUR SKILLS, LEAD YOUR TEAM, SAVE LIVES..</div>
  </div>
</header>

<section class="features">
  <h2>DON’T MISS THE PREMIER FIRE<br>&amp; RESCUE TRAINING EVENT</h2>
  <div class="cards">
    <article class="card">
      <div class="card-icon" role="img" aria-label="Icon of a helmet beside a flame"></div>
      <h3>LIVE FIRE<br>EXERCISES</h3>
      <p>Lorem ipsum dolor sit amet, consectetuer adipiscing elit, sed diam nonummy nibh euismod tincidunt ut laoreet</p>
    </article>
    <article class="card">
      <div class="card-icon" role="img" aria-label="Icon of a rope, gear and rescue tool"></div>
      <h3>HANDS-ON<br>RESCUE SCENARIOS</h3>
      <p>Lorem ipsum dolor sit amet, consectetuer adipiscing elit, sed diam nonummy nibh euismod tincidunt ut laoreet</p>
    </article>
    <article class="card">
      <div class="card-icon" role="img" aria-label="Icon of a shield with a clock"></div>
      <h3>CERTIFICATION<br>&amp; COMPLIANCE</h3>
      <p>Lorem ipsum dolor sit amet, consectetuer adipiscing elit, sed diam nonummy nibh euismod tincidunt ut laoreet</p>
    </article>
  </div>
</section>

<section class="cta">
  <h2>READY TO ADVANCE YOUR SKILLS?</h2>
  <div class="secure">Secure your Spot Today!</div>
  <a class="contact-link" href="#">Contact Marlowfield Crew Today</a>
  <hr>
  <div class="urgency">Limited Seats Available!<br>Early Bird Discounts End Soon!</div>
  <a class="register" href="#">REGISTER NOW</a>
  <div class="or">Or</div>
  <div class="details">CHECK COURSE DETAILS</div>
</section>

<footer class="footer">
  <div class="footer-brand">
    <span class="brand-dot"></span>
    <span class="brand-name">MARLOWFIELD CREW</span>
  </div>
  <div class="contact">
    <div>
      <svg viewBox="0 0 32 28" aria-hidden="true"><rect x="2" y="5" width="28" height="19" fill="none" stroke="#111" stroke-width="2.5"/><polyline points="2,5 16,16 30,5" fill="none" stroke="#111" stroke-width="2.5"/></svg>
      <span>info@marlowfieldcrew.com</span>
    </div>
    <div>
      <svg viewBox="0 0 32 28" aria-hidden="true"><path d="M9 3 L14 3 L15 9 L11 11 Q13 18 19 21 L21 17 L27 18 L27 24 Q14 26 7 14 Q5 8 9 3 Z" fill="#111"/></svg>
      <span>55501-24680</span>
    </div>
  </div>
  <div class="social" aria-label="Social media links">
    <span></span><span></span><span></span>
  </div>
</footer>

</body>
</html>
```